Waterjet Cutting Business requires an up to date website

We currently have a website which is outdated and in need of modernization.
We are only looking for a simple website with around 4 pages: Home, Contact Us, Materials, Gallery.
We have some pictures and a logo which can be used.
Our primary business is profile cutting of materials to customers specifications using high-pressure water with abrasive.
We are looking for creative ideas and are open to suggestions!
http://brightfordcutworks.com/index.asp?pid=1
Update:
Cut quality picture (uploaded)
Map
Comparison to other profile cutting methods such as plasma/laser
Single page style without continuous scrolling
"We can cut virtually any material from any drawing whether it be a Full 3D cad models to hand sketched "
Target Market(s)
Film Industry, Prototype, Engineering, Architect, Artisits, one off designs
Industry/Entity Type
Engineering
Number of Pages Required
1 page
Font styles to use
Look and feel

```html
<!DOCTYPE html>
<html lang="en">
<head>
<meta charset="utf-8">
<title>Brightford Cutworks – Waterjet Cutting Services</title>
<link rel="stylesheet" href="https://fonts.googleapis.com/css2?family=Montserrat:wght@400;600;700;800&family=Open+Sans:wght@400;600;700&family=Roboto+Condensed:wght@700&display=swap">
<style>
:root{
  --hero-deep:#0b3f8f;
  --hero-mid:#1766c4;
  --hero-light:#3b9be6;
  --nav:#0c5aa6;
  --accent:#1a9fd9;
  --orange:#f07a2c;
  --ink:#1d1d1d;
  --soft-blue:#7c94b8;
  --newsletter:#0a4f9c;
  --footer:#2b2b2b;
  --footer-bottom:#1c1c1c;
  --footer-text:#b5b5b5;
  --white:#ffffff;
}
*{margin:0;padding:0;box-sizing:border-box}
html,body{width:1200px;height:2965px;overflow:hidden}
body{position:relative;font-family:"Open Sans",Arial,sans-serif;color:var(--ink);background:var(--white)}
.abs{position:absolute}

.hero{left:0;top:0;width:1200px;height:637px;background:radial-gradient(ellipse at 65% 40%,var(--hero-light) 0%,var(--hero-mid) 45%,var(--hero-deep) 100%)}
.brand{display:flex;align-items:center;gap:12px;color:var(--white);font-family:"Montserrat",sans-serif;font-weight:800;font-size:27px;letter-spacing:1px}
.brand-mark{width:22px;height:22px;background:var(--white);border-radius:50%}
.header-brand{left:162px;top:30px}
.header-rule{left:0;top:95px;width:1200px;height:1px;background:rgba(255,255,255,.35)}
.header-info{display:flex;align-items:center;gap:14px;color:var(--white);font-size:11px;line-height:16px;font-weight:600}
.icon-ring{width:34px;height:34px;border:1.5px solid rgba(255,255,255,.8);border-radius:50%;display:flex;align-items:center;justify-content:center;flex:none}
.hero-arrows{left:162px;top:242px;display:flex;gap:6px}
.hero-arrows span{width:20px;height:20px;border:1.5px solid var(--white);border-radius:50%;display:flex;align-items:center;justify-content:center}
.hero-kicker{left:162px;top:288px;color:var(--white);font-family:"Montserrat",sans-serif;font-weight:700;font-size:12px;letter-spacing:.5px}
.hero-title{left:160px;top:314px;color:var(--white);font-family:"Montserrat",sans-serif;font-weight:700;font-size:51px;line-height:60px}
.hero-text{left:162px;top:455px;width:415px;color:var(--white);font-size:11.5px;line-height:19px}
.hero-dots{left:162px;top:522px;display:flex;gap:4px}
.hero-dots i{width:6px;height:6px;background:rgba(255,255,255,.6)}
.hero-dots i:first-child{background:var(--white)}
.hero-dots i:last-child{background:var(--orange)}

.main-nav{left:0;top:637px;width:1200px;height:53px;background:var(--nav)}
.nav-item{top:0;height:53px;display:flex;align-items:center;justify-content:center;color:var(--white);font-family:"Montserrat",sans-serif;font-weight:600;font-size:11px;border-right:1px solid rgba(255,255,255,.15)}
.nav-contact{left:739px;width:200px;background:var(--accent);font-size:15px;gap:10px}

.about-title{left:245px;top:757px;font-family:"Montserrat",sans-serif;font-weight:700;font-size:30px}
.section-rule{width:44px;height:3px;background:var(--ink)}
.btn{background:var(--accent);color:var(--white);font-family:"Montserrat",sans-serif;font-weight:700;font-size:10px;border-radius:16px;display:flex;align-items:center;justify-content:center}
.about-heading{left:472px;top:757px;width:500px;font-family:"Montserrat",sans-serif;font-weight:700;font-size:18px;line-height:22px}
.about-text{left:472px;top:820px;width:480px;font-size:11.3px;line-height:21px;color:var(--soft-blue)}

.materials{left:0;top:929px;width:1200px;height:593px;background:linear-gradient(135deg,#f6f6f6,#ececec 60%,#f4f4f4)}
.section-title{font-family:"Montserrat",sans-serif;font-weight:700;font-size:29px}
.photo-frame{border:1px solid #e3b89a;border-top:none;border-left:none}
.material-photo-a{background:linear-gradient(160deg,#0c2a2b,#0e6d5e 55%,#1fcfa7)}
.material-photo-b{background:linear-gradient(160deg,#101a4a,#2c4fc4 50%,#d24a82 85%,#1a2a6a)}
.materials-heading{left:686px;top:1110px;width:380px;font-family:"Roboto Condensed",sans-serif;font-weight:700;font-size:21px;line-height:29px}
.materials-text{left:686px;top:1186px;width:355px;font-size:11px;line-height:22.6px;color:#4a4a4a}

.gallery-card{top:1682px;width:166px}
.gallery-img{width:166px;height:143px}
.gallery-frame{position:absolute;left:14px;top:14px;width:166px;height:160px;border:1px solid #e0e0e0;background:var(--white);z-index:-1}
.gallery-caption{margin-left:36px;margin-top:8px;color:var(--orange);font-size:11px;font-weight:600}
.slider-dash{top:1900px;width:14px;height:3px;background:var(--nav)}

.newsletter{left:0;top:1977px;width:1200px;height:168px;background:var(--newsletter)}
.newsletter-title{left:160px;top:2030px;color:var(--white);font-family:"Montserrat",sans-serif;font-weight:700;font-size:28px}
.newsletter-lead{left:407px;top:2027px;color:var(--white);font-size:11.5px;font-weight:600}
.newsletter-input{left:407px;top:2060px;width:423px;height:32px;background:var(--white);font-size:11px;color:#888;padding-left:22px;display:flex;align-items:center}
.newsletter-btn{left:858px;top:2060px;width:180px;height:32px;font-size:10.5px}

.map{left:0;top:2145px;width:1200px;height:350px;background:linear-gradient(160deg,#d4d4d4,#bdbdbd 50%,#cfcfcf)}
.map-pin{left:578px;top:2297px;width:42px;height:42px;border-radius:50%;background:#222;color:var(--white);font-family:"Montserrat",sans-serif;font-size:16px;display:flex;align-items:center;justify-content:center}
.contact-card{left:453px;top:2396px;width:277px;height:283px;background:var(--white);border-top:3px solid var(--orange);box-shadow:0 2px 8px rgba(0,0,0,.2);z-index:2}
.card-title{position:absolute;top:30px;width:100%;text-align:center;color:var(--accent);font-family:"Montserrat",sans-serif;font-weight:700;font-size:12px}
.card-text{position:absolute;top:52px;left:30px;width:217px;text-align:center;font-size:11px;line-height:17px;font-weight:600}
.field{position:absolute;font-size:10px;color:#555;border-bottom:1px solid #999;height:18px}
.card-submit{position:absolute;left:65px;top:242px;width:146px;height:30px;background:var(--nav);font-size:11px}

.footer{left:0;top:2495px;width:1200px;height:431px;background:var(--footer)}
.footer-brand{left:162px;top:2555px}
.footer-about{left:162px;top:2613px;width:270px;color:var(--footer-text);font-size:11px;line-height:21px}
.footer-contact{left:751px;display:flex;align-items:flex-start;gap:16px;color:var(--footer-text);font-size:11px;line-height:19px}
.footer-contact .icon-ring{width:30px;height:30px;border-color:#888}
.footer-heading{top:2742px;color:var(--white);font-family:"Montserrat",sans-serif;font-weight:700;font-size:11px}
.footer-links{top:2780px;list-style:none;color:var(--footer-text);font-size:11px;line-height:22px}
.social{top:2782px;display:flex;gap:8px}
.social span{width:32px;height:32px;border:1.5px solid #bbb;border-radius:50%}
.footer-terms{left:886px;top:2832px;color:var(--footer-text);font-size:11px}
.footer-bottom{left:0;top:2926px;width:1200px;height:39px;background:var(--footer-bottom);color:var(--footer-text);font-size:11px;display:flex;align-items:center;justify-content:center}
</style>
</head>
<body>

<section class="abs hero" role="img" aria-label="Photograph of a waterjet cutting head and hoses, toned in blue"></section>
<div class="abs brand header-brand"><span class="brand-mark"></span>BRIGHTFORD</div>
<div class="abs header-info" style="left:600px;top:30px">
  <span class="icon-ring"><svg width="12" height="16" viewBox="0 0 12 16"><path d="M6 1a5 5 0 0 0-5 5c0 4 5 9 5 9s5-5 5-9a5 5 0 0 0-5-5zm0 7a2 2 0 1 1 0-4 2 2 0 0 1 0 4z" fill="#fff"/></svg></span>
  <span>Unit 7, Kestrel Court, Alder Lane, Fenwick Trade<br>Park, Oakhurst, Berks, OK4 9TL</span>
</div>
<div class="abs header-info" style="left:930px;top:30px">
  <span class="icon-ring"><svg width="14" height="14" viewBox="0 0 14 14"><path d="M3 1l2 3-1.3 1.5a8 8 0 0 0 4.8 4.8L10 9l3 2-1 2.5C6 13 1 8 .5 2z" fill="#fff"/></svg></span>
  <span>Phone :<br>01632 960418</span>
</div>
<div class="abs header-rule"></div>
<div class="abs hero-arrows">
  <span><svg width="6" height="8" viewBox="0 0 6 8"><path d="M5 0L0 4l5 4z" fill="#fff"/></svg></span>
  <span><svg width="6" height="8" viewBox="0 0 6 8"><path d="M1 0l5 4-5 4z" fill="#fff"/></svg></span>
</div>
<div class="abs hero-kicker">BRIGHTFORD CUTWORKS</div>
<h1 class="abs hero-title">Waterjet cutting<br>Services</h1>
<p class="abs hero-text">Brightford Cutworks is part of the Meridian Works Group who have been providing a model making and profile cutting service</p>
<div class="abs hero-dots"><i></i><i></i><i></i></div>

<nav class="abs main-nav">
  <a class="abs nav-item" style="left:162px;width:125px">HOME</a>
  <a class="abs nav-item" style="left:287px;width:157px">CONTACT US</a>
  <a class="abs nav-item" style="left:444px;width:150px">MATERIALS</a>
  <a class="abs nav-item" style="left:594px;width:145px">GALLERY</a>
  <a class="abs nav-item nav-contact">
    <svg width="26" height="22" viewBox="0 0 26 22"><path d="M4 3l3 4-1.8 2a11 11 0 0 0 6.5 6.5L13.7 14l4 3-1.3 3C8 20 1.5 13.5 1 4z" fill="#fff"/><rect x="15" y="1" width="10" height="8" rx="2" fill="none" stroke="#fff" stroke-width="1.5"/></svg>
    Contact Us</a>
  <a class="abs nav-item" style="left:939px;width:100px;border:none">
    <svg width="14" height="14" viewBox="0 0 14 14"><circle cx="7" cy="4" r="3.5" fill="#fff"/><path d="M0 14c0-4 3-6 7-6s7 2 7 6z" fill="#fff"/></svg></a>
</nav>

<h2 class="abs about-title">About Us</h2>
<div class="abs section-rule" style="left:245px;top:800px"></div>
<a class="abs btn" style="left:245px;top:844px;width:135px;height:32px">MORE INFORMATION</a>
<h3 class="abs about-heading">Waterjet Cutting Offers a Soloution Where Other Technologies Struggle</h3>
<p class="abs about-text">Brightford Cutworks is part of the Meridian Works Group who have been providing a modelmaking and profile cutting service primarily to the film industry for over 10 years. We are used toworking within tight timeframes with a fast turnaround for all aspects of Water....</p>

<section class="abs materials"></section>
<h2 class="abs section-title" style="left:162px;top:990px">Materials</h2>
<div class="abs section-rule" style="left:162px;top:1033px;width:24px;background:var(--nav)"></div>
<div class="abs photo-frame" style="left:172px;top:1099px;width:202px;height:344px"></div>
<div class="abs material-photo-a" style="left:162px;top:1089px;width:202px;height:344px" role="img" aria-label="Close-up photo of a waterjet nozzle cutting a metal sheet"></div>
<div class="abs photo-frame" style="left:409px;top:1099px;width:202px;height:344px"></div>
<div class="abs material-photo-b" style="left:399px;top:1089px;width:202px;height:344px" role="img" aria-label="Photo of a cutting head with coloured hoses"></div>
<h3 class="abs materials-heading">It is Possible to Cut Virtually any Profile in any Material with Waterjet</h3>
<p class="abs materials-text">Materials we can cut include, but are not limited to, all metals andalloys, stone and ceramics, composites, solid surface, wood, glass, acrylics, resins, silicones, plastics, foams, carpet and felts. We can also cut laminated dissimilar materials which can often be very hard to cut using conventional methods. We are always happyto test cut a sample of your material free of charge to demonstrate the quality of cut achievable. Employing Torrent's low pressure vacuum assist we can pierce and cut brittle materials such as acrylics and ceramics. In addition Adaptive Waterjet technology with Precision Taper Control produces more accurate parts at significantly higher cutting speeds than parts cut with a conventional waterjet.</p>

<h2 class="abs section-title" style="left:162px;top:1586px">Gallery</h2>
<div class="abs section-rule" style="left:162px;top:1628px;width:24px;background:var(--nav)"></div>
<div class="abs gallery-card" style="left:162px;z-index:1"><div class="gallery-frame"></div><div class="gallery-img" style="background:linear-gradient(150deg,#2a3550,#8fa3c4 50%,#39425a)" role="img" aria-label="Photo of a waterjet head over a cutting bed"></div><div class="gallery-caption">Waterjet Cutting Service</div></div>
<div class="abs gallery-card" style="left:393px;z-index:1"><div class="gallery-frame"></div><div class="gallery-img" style="background:linear-gradient(150deg,#0f2230,#2f6f86 55%,#14303e)" role="img" aria-label="Photo of a cutting head in teal light"></div><div class="gallery-caption">Waterjet Cutting Service</div></div>
<div class="abs gallery-card" style="left:625px;z-index:1"><div class="gallery-frame"></div><div class="gallery-img" style="background:linear-gradient(150deg,#0a2a0c,#2bb33a 55%,#0c3310)" role="img" aria-label="Photo of a cutting head in green light"></div><div class="gallery-caption">Waterjet Cutting Service</div></div>
<div class="abs gallery-card" style="left:856px;z-index:1"><div class="gallery-frame"></div><div class="gallery-img" style="background:linear-gradient(150deg,#2a0c08,#d0502a 55%,#3a1208)" role="img" aria-label="Photo of a cutting head in red light"></div><div class="gallery-caption">Waterjet Cutting Service</div></div>
<div class="abs slider-dash" style="left:574px"></div>
<div class="abs slider-dash" style="left:592px;background:#555"></div>
<div class="abs slider-dash" style="left:610px;background:#555"></div>

<section class="abs newsletter"></section>
<h2 class="abs newsletter-title">Newsletter</h2>
<div class="abs" style="left:160px;top:2074px;width:40px;height:2px;background:var(--white)"></div>
<p class="abs newsletter-lead">Subscribe to our Newsletter to Receive Latest&nbsp; News and Updates</p>
<div class="abs newsletter-input">Enter&nbsp; E-mail</div>
<a class="abs btn newsletter-btn">Subscribe To Newsletter</a>

<section class="abs map" role="img" aria-label="Street map showing the workshop location"></section>
<div class="abs map-pin">X</div>
<div class="abs contact-card">
  <div class="card-title">GET IN TOUCH</div>
  <p class="card-text">Lorem Ipsum is simply dummy text of the printing and typesetting industry</p>
  <div class="field" style="left:22px;top:112px;width:112px">First Name :</div>
  <div class="field" style="left:144px;top:112px;width:112px">Last Name :</div>
  <div class="field" style="left:22px;top:146px;width:112px">E-mail :</div>
  <div class="field" style="left:144px;top:146px;width:112px">Phone :</div>
  <div class="field" style="left:22px;top:180px;width:234px;height:36px">Message :</div>
  <a class="btn card-submit">SUBMIT</a>
</div>

<footer class="abs footer"></footer>
<div class="abs brand footer-brand"><span class="brand-mark"></span>BRIGHTFORD</div>
<p class="abs footer-about">Brightford Cutworks is part of the Meridian Works Group who have been providing a model making and profile cutting service primarily to the film industry...</p>
<div class="abs footer-contact" style="top:2550px">
  <span class="icon-ring"><svg width="12" height="12" viewBox="0 0 14 14"><path d="M3 1l2 3-1.3 1.5a8 8 0 0 0 4.8 4.8L10 9l3 2-1 2.5C6 13 1 8 .5 2z" fill="#ddd"/></svg></span>
  <span style="padding-top:5px">TELEPHONE&nbsp; : &nbsp;01632 960418</span>
</div>
<div class="abs footer-contact" style="top:2604px">
  <span class="icon-ring"><svg width="12" height="12" viewBox="0 0 12 12"><path d="M6 1L1 5.5h1.5V11h2.5V8h2v3h2.5V5.5H11z" fill="#ddd"/></svg></span>
  <span>Unit 7, Kestrel Court, Alder Lane, Fenwick<br>Trade Park, Oakhurst, Berks...</span>
</div>
<div class="abs footer-contact" style="top:2658px">
  <span class="icon-ring"><svg width="14" height="10" viewBox="0 0 14 10"><rect x=".5" y=".5" width="13" height="9" fill="none" stroke="#ddd"/><path d="M.5.5L7 6l6.5-5.5" fill="none" stroke="#ddd"/></svg></span>
  <span style="padding-top:5px">E-MAIL&nbsp; : &nbsp;info@brightfordcutworks.com</span>
</div>
<h4 class="abs footer-heading" style="left:162px">NAVIGATION</h4>
<ul class="abs footer-links" style="left:162px"><li>Home</li><li>Contact Us</li><li>Materials</li><li>Gallery</li></ul>
<h4 class="abs footer-heading" style="left:431px">QUICK LINKS</h4>
<ul class="abs footer-links" style="left:431px"><li>Blog</li><li>Support</li><li>Login</li><li>Account</li></ul>
<ul class="abs footer-links" style="left:652px"><li>Contact</li><li>Portfolio</li><li>News</li><li>Sign Up</li></ul>
<h4 class="abs footer-heading" style="left:886px">SOCIAL LINKS</h4>
<div class="abs social" style="left:884px"><span></span><span></span><span></span><span></span></div>
<p class="abs footer-terms">Terms and Condition</p>
<div class="abs footer-bottom">Copyright © 2016 Brightford Cutworks.&nbsp; All rights reserved &nbsp; | &nbsp; Privacy Policy</div>

</body>
</html>
```